Social Media Advert for Office Fruit Delivery in Dubai

We need an attractive design for social media adverts, for delivering assorted fruit boxes to companies. We will be delivering costume package fruit boxes, with great price, and great quality. Our fruit boxes is +4.5 kg and includes apples, bananas, kiwis, some citrus, and some stone fruit depending on seasonality. Our offer prices are AED 45, which is very competitive as we are wholesalers, and growers of some of our fruits. Our goal is to support health initiative set by responsible companies. Our delivery is free for companies who enrol into weekly delivery programs restricted to Dubai only. We suggest deliveries to be once a week, as our fruit is fresh, and great for consumption in a one week window. Considering each employee on average would consume two pieces of fruits a day, our fruit boxes is ideal for 4 employees in one working week. We need a talented designer, to kick start our sales. You can find more details about this project, and about our company on our website www.lunagrove.co follow us on social media @lunagroveuae

Target Market(s)

age 22-50, based in Dubai working individuals in companies with responsibility to care for it's employees and their health.

Font styles to use
Other font styles liked:
• IYC Avant Garde Gothic LT Bold

Colors

Designer to choose colors to be used in the design.

Requirements
Must have
• - Logo
• - offer price and product
Nice to have
• Check out the 'inspire' in attachments to understand what we are looking for

```html
<!DOCTYPE html>
<html lang="en">
<head>
<meta charset="utf-8">
<title>Luna Grove – Farm Fresh On Your Desk</title>
<link rel="stylesheet" href="https://fonts.googleapis.com/css2?family=Montserrat:wght@400;500;600;700&family=Righteous&display=swap">
<style>
  :root{
    --stage:#2b2b2b;
    --cream:#f6f8dc;
    --green:#7cb82f;
    --orange:#e8562a;
    --yellow:#f4e84a;
    --ink:#2a2a2a;
    --leaf:#3f6b24;
    --orchard:#6f9a3a;
    --fruit:#e5772a;
    --sky:#cfdce8;
  }
  *{margin:0;padding:0;box-sizing:border-box}
  html,body{width:1200px;height:800px;overflow:hidden;background:var(--stage)}
  body{font-family:"Montserrat",Arial,sans-serif;color:var(--ink)}
  .flyer{position:absolute;left:300px;top:12px;width:600px;height:776px;background:var(--cream);overflow:hidden}
  .hero{position:absolute;left:0;top:0;width:600px;height:313px;display:block}
  .abs{position:absolute}
  .brand{left:141px;top:328px;width:68px;height:68px;border-radius:50%;background:var(--yellow);
    display:flex;align-items:center;justify-content:center;text-align:center;
    font-weight:700;font-size:12px;line-height:1.1;color:var(--orange)}
  .headline{left:226px;top:331px;font-family:"Righteous",Arial,sans-serif;letter-spacing:3px;line-height:1}
  .headline .top{display:block;font-size:31px;color:var(--green)}
  .headline .bottom{display:block;font-size:22px;color:var(--orange);margin-top:4px;letter-spacing:5px}
  .intro{left:0;width:600px;top:410px;text-align:center;font-size:11px;line-height:18px;letter-spacing:.3px;text-transform:uppercase}
  .intro em{font-style:normal;color:var(--orange);font-weight:600}
  .step{width:180px;text-align:center}
  .step .icon{width:58px;height:58px;margin:0 auto;display:block}
  .step h3{margin-top:20px;font-size:11px;font-weight:700;color:var(--green);letter-spacing:.8px;padding-bottom:5px;border-bottom:1px solid var(--orange)}
  .step p{margin-top:6px;font-size:7px;line-height:11.5px;text-transform:uppercase}
  .step p.big{font-size:8px;line-height:11.5px}
  .step .accent{color:var(--orange);font-weight:600}
  .step .accent.lg{font-size:10.5px;font-weight:600}
  .social{left:0;width:600px;top:642px;text-align:center;font-size:11.5px;letter-spacing:.5px}
  .badges{left:0;width:600px;top:672px;display:flex;justify-content:center;gap:20px}
  .badge{width:38px;height:38px;border-radius:50%;border:2px solid var(--orange);background:transparent}
  .contact{left:0;width:600px;top:722px;display:flex;justify-content:center;align-items:center;gap:12px;font-size:12px;letter-spacing:.6px}
  .contact .sep{color:var(--orange)}
  .contact svg{vertical-align:middle;margin-right:8px}
  .address{left:0;width:600px;top:749px;text-align:center;font-size:12px;letter-spacing:.6px}
  .address svg{vertical-align:middle;margin-right:12px}
</style>
</head>
<body>
<main class="flyer">
  <svg class="hero" viewBox="0 0 600 313" role="img" aria-label="Photo of ripe tangerines hanging on a tree in a green orchard, with an inset photo of a fruit delivery truck">
    <defs>
      <linearGradient id="orchardFill" x1="0" y1="0" x2="0" y2="1">
        <stop offset="0" stop-color="var(--sky)"/>
        <stop offset=".2" stop-color="var(--leaf)"/>
        <stop offset=".75" stop-color="var(--leaf)"/>
        <stop offset="1" stop-color="var(--orchard)"/>
      </linearGradient>
      <radialGradient id="fruitGlow" cx=".6" cy=".45" r=".45">
        <stop offset="0" stop-color="var(--fruit)" stop-opacity=".55"/>
        <stop offset="1" stop-color="var(--fruit)" stop-opacity="0"/>
      </radialGradient>
      <linearGradient id="truckFill" x1="0" y1="0" x2="0" y2="1">
        <stop offset="0" stop-color="var(--sky)"/>
        <stop offset=".55" stop-color="#5d8a38"/>
        <stop offset="1" stop-color="var(--orchard)"/>
      </linearGradient>
    </defs>
    <rect width="600" height="313" fill="url(#orchardFill)"/>
    <rect width="600" height="313" fill="url(#fruitGlow)"/>
    <path d="M0 75 H200 A92 92 0 0 1 200 259 H0 Z" fill="url(#truckFill)" stroke="#fff" stroke-width="2"/>
  </svg>

  <div class="abs brand">Luna<br>Grove</div>
  <h1 class="abs headline"><span class="top">FARM FRESH</span><span class="bottom">ON YOUR DESK</span></h1>

  <p class="abs intro">We are bringing from <em>fresh fruits</em> right to your ofice.<br>Create your own custom crate or we’ll hand select<br>the best flavors in one convenient box!</p>

  <section class="abs step" style="left:18px;top:478px">
    <svg class="icon" viewBox="0 0 58 58" aria-hidden="true">
      <circle cx="29" cy="29" r="27.5" fill="none" stroke="var(--green)" stroke-width="2"/>
      <path d="M16 20h5l4 14h14l3-10H23" fill="none" stroke="var(--orange)" stroke-width="3" stroke-linejoin="round"/>
      <circle cx="27" cy="39" r="2.5" fill="var(--orange)"/><circle cx="37" cy="39" r="2.5" fill="var(--orange)"/>
    </svg>
    <h3>FIND YOUR FAVORITES ...</h3>
    <p>You can plan a compination of<br>fruits depending on yor prefrenence or<br>you can choose our best selling assorted<br>box of fruits&nbsp; AED 45.00 (net wt 4.5kg)</p>
  </section>

  <section class="abs step" style="left:198px;top:478px">
    <svg class="icon" viewBox="0 0 58 58" aria-hidden="true">
      <circle cx="29" cy="29" r="27.5" fill="none" stroke="var(--green)" stroke-width="2"/>
      <path d="M15 24c0-5 28-5 28 0v3h-7v-3H22v3h-7z" fill="var(--orange)"/>
      <path d="M19 29h20l3 12H16z" fill="var(--orange)"/>
      <circle cx="29" cy="35" r="3" fill="var(--cream)"/>
    </svg>
    <h3>PLACE YOUR ORDER ....</h3>
    <p class="big">Call us directtly<br><span class="accent lg">+971 4 555 0190</span> or visit<br>our online store at<br><span class="accent">www.lunagrove.co/fruitdelivery</span></p>
  </section>

  <section class="abs step" style="left:398px;top:478px">
    <svg class="icon" viewBox="0 0 58 58" aria-hidden="true">
      <circle cx="29" cy="29" r="27.5" fill="none" stroke="var(--green)" stroke-width="2"/>
      <rect x="13" y="21" width="20" height="14" fill="var(--orange)"/>
      <path d="M34 25h6l5 5v5H34z" fill="var(--orange)"/>
      <circle cx="20" cy="37" r="3" fill="var(--orange)" stroke="var(--cream)" stroke-width="1.5"/>
      <circle cx="39" cy="37" r="3" fill="var(--orange)" stroke="var(--cream)" stroke-width="1.5"/>
    </svg>
    <h3>W’LL BRING IT TO YOU ...</h3>
    <p class="big">Get your fruits package within<br><span class="accent lg">30 MINUTES</span> ofter your order<br>free delivery!</p>
  </section>

  <p class="abs social">@LUNAGROVEUAE</p>

  <div class="abs badges" role="img" aria-label="Quality seals">
    <span class="badge"></span><span class="badge"></span><span class="badge"></span>
  </div>

  <div class="abs contact">
    <span><svg width="15" height="15" viewBox="0 0 24 24" aria-hidden="true"><path d="M6 2l4 4-2 3c1 3 4 6 7 7l3-2 4 4-3 4C10 22 2 14 2 5z" fill="var(--orange)"/></svg>+971 4 555 0190</span>
    <span class="sep">|</span>
    <span><svg width="14" height="14" viewBox="0 0 24 24" aria-hidden="true"><circle cx="12" cy="12" r="10" fill="none" stroke="var(--orange)" stroke-width="2.5"/><path d="M2 12h20M12 2c-5 6-5 14 0 20M12 2c5 6 5 14 0 20" fill="none" stroke="var(--orange)" stroke-width="1.8"/></svg>WWW.LUNAGROVE.CO</span>
    <span class="sep">|</span>
    <span><svg width="17" height="13" viewBox="0 0 24 18" aria-hidden="true"><rect x="1" y="1" width="22" height="16" fill="none" stroke="var(--orange)" stroke-width="2"/><path d="M1 1l11 9 11-9" fill="none" stroke="var(--orange)" stroke-width="2"/></svg>INFO@LUNAGROVE.CO</span>
  </div>

  <p class="abs address"><svg width="18" height="20" viewBox="0 0 24 26" aria-hidden="true"><path d="M12 1a7 7 0 0 1 7 7c0 5-7 12-7 12S5 13 5 8a7 7 0 0 1 7-7z" fill="var(--orange)"/><circle cx="12" cy="8" r="2.5" fill="var(--cream)"/><ellipse cx="12" cy="22" rx="9" ry="3" fill="none" stroke="var(--orange)" stroke-width="1.8"/></svg>PALM COURT MARKET , WAREHOUSE 12 &amp; 14 ,&nbsp; DUBAI , UAE</p>
</main>
</body>
</html>
```